Silver Lantern Restaurant
Silver Lantern Restaurant Stationery - Food
Silver Lantern Restaurant Stationery
Modern
Khalid Bazzour
CEO
Phone: 012 7318465 012 7352941 487 Jeddah 21833 Rawdah St. North from Jeddah Harbor Plaza
info@silverlantern-dining.example
www.silverlantern-dining.example
Requirements: 1. Business card 2. Letterhead 3. Envelope (DL only) check attached image 4. Notepad 5. cake box - check attached image 6. Cardboard Paper Bag
Design
rimasoufek rimasoufek
Thanks to everyone really nice work, but please don't submit business card solo, I don't need all stationery i need only what's mentioned in additional comments section in the brief.

```html
<!DOCTYPE html>
<html lang="en">
<head>
<meta charset="utf-8">
<title>Silver Lantern Restaurant — Business Card</title>
<link href="https://fonts.googleapis.com/css2?family=Montserrat:wght@400;600;700&display=swap" rel="stylesheet">
<style>
  :root {
    --page-bg: #e4e3e1;
    --card-bg: #ffffff;
    --ink: #2b2b2b;
    --ink-soft: #6b6b6b;
    --gold: #c98a1c;
    --gold-light: #f2c25a;
    --icon-bg: #2f2f2f;
  }
  * { margin: 0; padding: 0; box-sizing: border-box; }
  html, body {
    width: 1200px; height: 896px; overflow: hidden;
    background: var(--page-bg);
    font-family: "Montserrat", sans-serif;
    color: var(--ink);
  }
  .stage {
    position: relative; width: 1200px; height: 896px;
    display: flex; align-items: center; justify-content: center; gap: 44px;
  }
  .card {
    position: relative; width: 520px; height: 310px;
    background: var(--card-bg);
    border-radius: 10px 40px 10px 40px;
    box-shadow: 0 14px 30px rgba(0,0,0,0.22);
  }
  .card-back { display: flex; padding: 34px 30px 34px 34px; }
  .identity {
    width: 50%; display: flex; flex-direction: column; justify-content: flex-end;
  }
  .brand { display: flex; align-items: center; gap: 10px; margin-bottom: 22px; }
  .brand-dot {
    flex: none; width: 46px; height: 46px; border-radius: 50%;
    background: radial-gradient(circle at 35% 35%, var(--gold-light), var(--gold));
  }
  .brand-name { font-weight: 700; font-size: 17px; color: var(--gold); }
  .person-name { font-weight: 700; font-size: 17px; letter-spacing: 1px; text-transform: uppercase; }
  .person-title { font-size: 10px; letter-spacing: 1.5px; text-transform: uppercase; color: var(--ink-soft); margin-top: 4px; }
  .contacts {
    width: 50%; display: flex; flex-direction: column; justify-content: center; gap: 22px;
  }
  .contact-row { display: flex; align-items: flex-start; gap: 12px; }
  .contact-icon {
    flex: none; width: 24px; height: 24px; border-radius: 5px;
    background: var(--icon-bg); display: flex; align-items: center; justify-content: center;
  }
  .contact-text { font-size: 10px; line-height: 1.55; color: var(--ink); }
  .card-front { display: flex; align-items: center; justify-content: center; gap: 16px; }
  .card-front .brand-dot { width: 92px; height: 92px; }
  .card-front .brand-name { font-size: 30px; }
</style>
</head>
<body>
<main class="stage">
  <section class="card card-back" aria-label="Business card back">
    <div class="identity">
      <div class="brand">
        <span class="brand-dot"></span>
        <span class="brand-name">Silver Lantern</span>
      </div>
      <p class="person-name">Khalid Bazzour</p>
      <p class="person-title">CEO</p>
    </div>
    <div class="contacts">
      <div class="contact-row">
        <span class="contact-icon">
          <svg width="14" height="14" viewBox="0 0 24 24"><path fill="#fff" d="M6.6 10.8a15.1 15.1 0 0 0 6.6 6.6l2.2-2.2a1 1 0 0 1 1-.25 11.4 11.4 0 0 0 3.6.57 1 1 0 0 1 1 1V20a1 1 0 0 1-1 1A17 17 0 0 1 3 4a1 1 0 0 1 1-1h3.5a1 1 0 0 1 1 1c0 1.25.2 2.45.57 3.57a1 1 0 0 1-.25 1z"/></svg>
        </span>
        <p class="contact-text">012 7318465<br>012 7352941</p>
      </div>
      <div class="contact-row">
        <span class="contact-icon">
          <svg width="14" height="14" viewBox="0 0 24 24" fill="none" stroke="#fff" stroke-width="2"><circle cx="12" cy="12" r="9"/><path d="M3 12h18M12 3c3 3 3 15 0 18M12 3c-3 3-3 15 0 18"/></svg>
        </span>
        <p class="contact-text">www.silverlantern-dining.example<br>info@silverlantern-dining.example</p>
      </div>
      <div class="contact-row">
        <span class="contact-icon">
          <svg width="14" height="14" viewBox="0 0 24 24"><path fill="#fff" d="M12 2a7 7 0 0 0-7 7c0 5 7 13 7 13s7-8 7-13a7 7 0 0 0-7-7zm0 9.5A2.5 2.5 0 1 1 12 6.5a2.5 2.5 0 0 1 0 5z"/></svg>
        </span>
        <p class="contact-text">487 Jeddah 21833 Rawdah St.<br>North from Jeddah Harbor Plaza</p>
      </div>
    </div>
  </section>

  <section class="card card-front" aria-label="Business card front">
    <span class="brand-dot"></span>
    <span class="brand-name">Silver Lantern</span>
  </section>
</main>
</body>
</html>
```